Website for Private Psychologist

DO NOT CONTACT ME PRIVATELY

I am a Psychologist offering psychotherapy for individuals and couples, and clinical consultation and training and education for mental and medical health professionals and agencies.

I need a redesign of my website

5 Pages (content is attached for each page)
Home
Jungian Psychotherapy
Clinical Consultation & Professional Development
Curriculum Vitae & Publications
Practice Policies and Forms

Designs can be based on these style websites
https://lqmindcare.info; https://pdtarn.org/; https://dorabellcroftcounselling.com/

Design Concepts
Minimalist Layout: Clean and uncluttered layout with generous white space, allowing the content and visuals to stand out'

Keep a linear, uncluttered, professional design.

Please use only royalty free images and google fonts. Please provide links to any stock images used to verify license.

Target Market(s)

private individual or couples seeking psychotherapy

Industry/Entity Type

Psychotherapy

Number of Pages Required

5+ page

Requirements
Should not have
• No search feature

```html
<!DOCTYPE html>
<html lang="en">
<head>
<meta charset="utf-8">
<title>Daniel Marlowe, Psy.D. — Jungian Psychotherapy</title>
<link href="https://fonts.googleapis.com/css2?family=Playfair+Display:wght@700&family=Poppins:wght@300;400;500;600;700;800&display=swap" rel="stylesheet">
<style>
  :root {
    --ink: #2b2b2b;
    --ink-soft: #3a3a3a;
    --green: #1b8a57;
    --white: #ffffff;
    --dots: #d2d2d2;
  }
  * { box-sizing: border-box; margin: 0; padding: 0; }
  html, body { width: 1200px; height: 775px; overflow: hidden; background: var(--white); }
  body { position: relative; font-family: "Poppins", sans-serif; color: var(--ink); }

  .sidebar-toggle {
    position: absolute; left: 366px; top: 14px; width: 23px; height: 23px;
    background: var(--ink); display: flex; align-items: center; justify-content: center;
  }
  .sidebar-divider { position: absolute; left: 377px; top: 59px; width: 3px; height: 609px; background: var(--ink); }

  .brand { position: absolute; left: 0; width: 376px; top: 66px; text-align: center; }
  .brand-name { font-weight: 800; font-size: 21px; letter-spacing: -0.2px; color: var(--ink); }
  .brand-licence { font-size: 11.5px; font-weight: 400; color: var(--ink-soft); margin-top: 4px; }

  .main-nav { position: absolute; left: 53px; width: 271px; top: 0; }
  .nav-item {
    position: absolute; left: 0; width: 271px; text-align: center;
    font-size: 12.4px; font-weight: 500; line-height: 16px; color: var(--ink); text-transform: uppercase;
  }
  .nav-item.is-active {
    background: var(--green); color: var(--white); font-weight: 700;
    height: 58px; display: flex; align-items: center; justify-content: center;
  }

  .sidebar-rule { position: absolute; left: 41px; top: 517px; width: 297px; height: 3px; background: var(--ink); }

  .contact { position: absolute; left: 46px; font-size: 14.2px; font-weight: 300; line-height: 20px; color: var(--ink); }
  .contact-icon { position: absolute; left: 0; top: 4px; }
  .contact-text { padding-left: 20px; }
  .contact strong { font-weight: 700; }

  .dot-field { position: absolute; left: 1084px; top: 30px; width: 84px; height: 83px; background: var(--dots); }

  .page-content { position: absolute; left: 448px; top: 283px; width: 620px; }
  .page-title { font-family: "Playfair Display", serif; font-weight: 700; font-size: 40px; color: var(--ink); line-height: 1.2; }
  .page-intro { margin-top: 14px; font-size: 14.2px; font-weight: 300; line-height: 20.5px; color: var(--ink); }

  .site-footer { position: absolute; left: 0; width: 1200px; top: 706px; text-align: center; font-size: 13.8px; font-weight: 500; color: var(--ink); }
  .site-footer p + p { margin-top: 7px; }
  .site-footer a { color: var(--green); font-weight: 700; text-decoration: none; border-bottom: 1px solid var(--green); }

  .back-to-top {
    position: absolute; left: 1133px; top: 711px; width: 40px; height: 40px; border-radius: 50%;
    background: var(--green); display: flex; align-items: center; justify-content: center;
  }
</style>
</head>
<body>
  <a class="sidebar-toggle" href="#" aria-label="Collapse sidebar">
    <svg width="11" height="9" viewBox="0 0 11 9"><path d="M10.5 4.5H1M4.5 1L1 4.5 4.5 8" stroke="#fff" stroke-width="1.1" fill="none"/></svg>
  </a>

  <header class="brand">
    <h1 class="brand-name">Daniel Marlowe, Psy.D.</h1>
    <p class="brand-licence">California Licensed Psychologist PSY 48172</p>
  </header>

  <nav class="main-nav">
    <a class="nav-item" style="top:180px">Home</a>
    <a class="nav-item is-active" style="top:228px">Jungian<br>Psychotherapy</a>
    <a class="nav-item" style="top:303px">Clinical Consultation &amp;<br>Professional Development</a>
    <a class="nav-item" style="top:364px">Curriculum Vitae<br>and Publications</a>
    <a class="nav-item" style="top:424px">Practice Policies<br>and Forms</a>
  </nav>

  <div class="sidebar-rule"></div>

  <div class="contact" style="top:569px">
    <svg class="contact-icon" width="13" height="13" viewBox="0 0 24 24"><path fill="#1b8a57" d="M6.6 10.8a15.1 15.1 0 0 0 6.6 6.6l2.2-2.2c.3-.3.7-.4 1-.2 1.1.4 2.3.6 3.6.6.6 0 1 .4 1 1V20c0 .6-.4 1-1 1A17 17 0 0 1 3 4c0-.6.4-1 1-1h3.5c.6 0 1 .4 1 1 0 1.3.2 2.5.6 3.6.1.3 0 .7-.2 1z"/></svg>
    <p class="contact-text">To schedule an initial consultation please<br>&nbsp;contact me at &nbsp;<strong>(555) 014-2290</strong></p>
  </div>
  <div class="contact" style="top:629px">
    <svg class="contact-icon" width="13" height="11" viewBox="0 0 24 20" style="top:6px"><path fill="#1b8a57" d="M0 2v2l12 7 12-7V2zM0 6.5V18h24V6.5L12 13.5z"/></svg>
    <p class="contact-text">Or email<br><strong>info@danielmarlowe.com</strong></p>
  </div>

  <div class="sidebar-divider"></div>

  <div class="dot-field" role="img" aria-label="Decorative dot grid"></div>

  <main class="page-content">
    <h2 class="page-title">Jungian Psychotherapy</h2>
    <p class="page-intro">I practice depth-oriented psychotherapy and tailor my approach to the individual or couple seeking treatment.&nbsp; I have experience treating a range of psychological issues including depression, anxiety, and relationship and job dissatisfaction as well as life transition issues such as college and graduate school stress, pre-marital counseling, and issues related to identity and sexuality.</p>
  </main>

  <footer class="site-footer">
    <p>For more information about analytical psychology please visit the <a href="https://pdtarn.org/">Pacific Depth Training Institute.</a></p>
    <p>© Daniel Marlowe 2023</p>
  </footer>

  <a class="back-to-top" href="#" aria-label="Back to top">
    <svg width="9" height="6" viewBox="0 0 9 6"><path d="M1 5l3.5-3.5L8 5" stroke="#fff" stroke-width="1.4" fill="none"/></svg>
  </a>
</body>
</html>
```